Real Estate Card Design

I need a new business card! Below you will find my headshot, the company logo and a copy of my previous business card.

The card must contain the following information:

Dana Welch
Sales Representative
FAIR HARBOUR HOMES REALTY INC BROKERGE
204-517 Maple Ave E, Oshawa ON L1G 4K7
Cell: 905-618-4037 Office:905-481-2696
www.danawelch.com dana@movewithwelch.ca

I would like the card to portray security and class all the while being fresh and contemporary. I hold the key....

```html
<!DOCTYPE html>
<html lang="en">
<head>
<meta charset="utf-8">
<title>Dana Welch – Business Card</title>
<link rel="stylesheet" href="https://fonts.googleapis.com/css2?family=Montserrat:wght@600&family=PT+Sans:wght@400;700&display=swap">
<style>
  :root {
    --page: #e6e6e8;
    --card-dark: #0f1319;
    --card-mid: #232a33;
    --accent: #1a9fdb;
    --text-main: #f2f4f6;
    --text-soft: #d4d8dd;
    --photo-hair: #c9ad84;
    --photo-skin: #a98573;
    --photo-suit: #1d2430;
  }
  * { margin: 0; padding: 0; box-sizing: border-box; }
  html, body {
    width: 1200px; height: 900px; overflow: hidden;
    background: var(--page);
  }
  .card {
    position: absolute; left: 75px; top: 150px;
    width: 1050px; height: 600px;
    background: radial-gradient(ellipse at 45% 40%, var(--card-mid) 0%, var(--card-dark) 75%);
    box-shadow: 0 12px 30px rgba(0,0,0,0.25);
    overflow: hidden;
    font-family: "PT Sans", sans-serif;
    color: var(--text-main);
  }
  .brand {
    position: absolute; left: 55px; top: 48px;
    display: flex; align-items: center; gap: 16px;
  }
  .brand-mark { width: 58px; height: 58px; background: var(--accent); flex: none; }
  .brand-name {
    font-family: "Montserrat", sans-serif; font-weight: 600;
    font-size: 22px; line-height: 1.25; letter-spacing: 1px;
    color: var(--text-main); text-transform: uppercase;
  }
  .agent-name {
    position: absolute; left: 55px; top: 238px;
    font-family: "Montserrat", sans-serif; font-weight: 600;
    font-size: 50px; letter-spacing: 0.5px; color: var(--text-main);
  }
  .agent-role {
    position: absolute; left: 57px; top: 306px;
    font-size: 21px; color: var(--text-soft);
    padding-bottom: 6px; border-bottom: 3px solid var(--accent);
  }
  .contact-list {
    position: absolute; left: 45px; top: 428px;
    list-style: none;
  }
  .contact-list li {
    display: flex; align-items: center; gap: 14px;
    height: 32px; font-size: 19px; color: var(--text-main);
    white-space: nowrap;
  }
  .contact-list .label { color: var(--text-soft); }
  .contact-list .icon { width: 22px; height: 22px; flex: none; }
  .contact-list .office { font-size: 14px; font-weight: 700; }
  .contact-list .address {
    height: 22px; padding-left: 36px; font-size: 11px; font-weight: 700;
  }
  .agent-photo {
    position: absolute; left: 620px; top: 20px; width: 420px; height: 580px;
    background:
      linear-gradient(to right, var(--card-dark) 0%, rgba(15,19,25,0) 22%),
      linear-gradient(to bottom, rgba(15,19,25,0) 0%, var(--photo-hair) 8%, var(--photo-skin) 30%, var(--photo-suit) 52%, var(--card-dark) 100%);
    border-radius: 180px 180px 0 0;
  }
</style>
</head>
<body>
  <div class="card">
    <div class="brand">
      <div class="brand-mark"></div>
      <div class="brand-name">Fair Harbour Homes<br>Realty Inc.</div>
    </div>

    <h1 class="agent-name">DANAWELCH</h1>
    <p class="agent-role">Sales Representative</p>

    <ul class="contact-list">
      <li>
        <svg class="icon" viewBox="0 0 22 22"><circle cx="11" cy="11" r="11" fill="var(--accent)"/><path d="M7.5 6.5l2 0 1 2.6-1.3 1a6 6 0 0 0 2.7 2.7l1-1.3 2.6 1 0 2a1 1 0 0 1-1 1A9 9 0 0 1 6.5 7.5a1 1 0 0 1 1-1z" fill="#fff"/></svg>
        <span><span class="label">Cell:</span> 905-618-4037 &nbsp;<span class="label">Office:</span> 905-481-2696</span>
      </li>
      <li>
        <svg class="icon" viewBox="0 0 22 22"><circle cx="11" cy="11" r="11" fill="var(--accent)"/><rect x="5.5" y="7" width="11" height="8" fill="#fff"/><path d="M5.5 7l5.5 4.5L16.5 7" fill="none" stroke="var(--accent)" stroke-width="1.3"/></svg>
        <span>dana@movewithwelch.ca</span>
      </li>
      <li>
        <svg class="icon" viewBox="0 0 22 22"><circle cx="11" cy="11" r="11" fill="var(--accent)"/><path d="M8 5.5l0 10.5 2.6-2.5 1.8 3.6 1.6-.8-1.8-3.5 3.6-.3z" fill="#fff"/></svg>
        <span>www.danawelch.com</span>
      </li>
      <li>
        <svg class="icon" viewBox="0 0 22 22"><circle cx="11" cy="11" r="11" fill="var(--accent)"/><path d="M7.5 6.5l2 0 1 2.6-1.3 1a6 6 0 0 0 2.7 2.7l1-1.3 2.6 1 0 2a1 1 0 0 1-1 1A9 9 0 0 1 6.5 7.5a1 1 0 0 1 1-1z" fill="#fff"/></svg>
        <span class="office">FAIR HARBOUR HOMES REALTY INC BROKERGE</span>
      </li>
      <li class="address">204-517 Maple Ave E, Oshawa ON L1G 4K7</li>
    </ul>

    <div class="agent-photo" role="img" aria-label="Portrait of the sales representative in a pinstripe suit, holding up a house key"></div>
  </div>
</body>
</html>
```